Ferrolix - Train Delay Compensation. We help cummuters in the uk using national rail get there money

We help train commuter who pay very high price for their rail ticket.on Weekly, Monthly and yearly ticket) get some of their money back when their train is delayed or cancelled up to a max of £300 per month all they need to do is download our app from the app store app or android of visit our website www.ferrolix-example.com . The get back up to 40% the cost of their ticket . No claim no fee!! Unlimited claims !! No form filling , No printing no posting we do all the work just claim and wait for your money through the post.
Task
A6 Size paper design and wordings over the 2 pages front and back . wording should include high impact words like ' Don't be short changed ' ' It's your money get it back!! ' The big deal Get up to 40% of cost of ticket back' ' No claim no fee!' preferable should include on the front page picture of crowd of people packed tight on the train or stuck at a train station. Uk Pictures only please . I have a vector image of the logo of out company if needed will upload a jpeg now

with our app they will get possible claim notifications when their trains is late and they are in line for a compensation which can be between 50% to 100% the cost of a daily ticket

Target Market(s)

train commuter in the uk

Requirements
Must have
• No claim no fee.,The big deal Get up to 40% of cost of ticket back' max of £300 per month. Don't be short changed get it's your money get it back. download out app and we do the rest free trial ! . No filling forms , printing or posting of forms we do all the work for you. Just click claim and wait for your money thorough the post. No claim no fee!! Unlimited claims !! No form filling , No printing no posting we do all the work just claim and wait for your money through the post.
• Logo of the company. Must be high impact and attention grabbing !!
Nice to have
• Pictures of commuters packed in the train. Picture of commuters stranded at the train station because of delayed or cancelled trains.

```html
<!DOCTYPE html>
<html lang="en">
<head>
<meta charset="utf-8">
<title>Ferrolix – Train Delay Compensation Flyer</title>
<link href="https://fonts.googleapis.com/css2?family=Oswald:wght@400;500;600;700&family=Questrial&display=swap" rel="stylesheet">
<style>
  :root {
    --navy: #1c2a68;
    --red: #d21f2b;
    --paper: #f5f3f8;
    --backdrop: #e8e4e4;
    --photo-train-a: #6b5a55;
    --photo-train-b: #2f2b33;
    --photo-station-a: #8a7a62;
    --photo-station-b: #3b3431;
  }
  * { box-sizing: border-box; margin: 0; padding: 0; }
  html, body { width: 1200px; height: 811px; overflow: hidden; }
  body { background: var(--backdrop); position: relative; font-family: 'Questrial', sans-serif; }

  .page {
    position: absolute; top: 87px; width: 450px; height: 636px;
    background: var(--paper); overflow: hidden;
    box-shadow: 0 6px 18px rgba(0,0,0,.18);
  }
  .page--front { left: 140px; }
  .page--back { left: 610px; }

  .headline {
    position: absolute; font-family: 'Oswald', sans-serif; font-weight: 600;
    line-height: 1; text-transform: uppercase; color: var(--navy);
  }
  .headline .accent { color: var(--red); }
  .page--front .headline { left: 14px; top: 28px; font-size: 44px; transform: rotate(-4deg); transform-origin: left top; }
  .page--front .headline .line2 { font-size: 52px; }
  .page--back .headline { right: 12px; top: 32px; font-size: 34px; transform: rotate(4deg); transform-origin: right top; text-align: left; }
  .page--back .headline .line2 { font-size: 44px; }

  .rule {
    position: absolute; left: 0; width: 100%; height: 5px;
    border-top: 2px dashed var(--red); border-bottom: 2px solid var(--navy);
  }
  .rule--top { top: 142px; }
  .rule--bottom { top: 472px; transform: rotate(-1.5deg); }
  .page--back .rule--bottom { transform: rotate(1.5deg); }

  .photo { position: absolute; left: 0; top: 148px; width: 450px; height: 330px; }
  .photo--train { background: linear-gradient(180deg, var(--photo-train-a) 0%, var(--photo-train-b) 55%, #7a2b36 100%); }
  .photo--station { background: linear-gradient(180deg, #9c8a70 0%, var(--photo-station-a) 30%, var(--photo-station-b) 75%, #7a2b36 100%); }

  .wave { position: absolute; left: 0; top: 368px; width: 450px; height: 110px; }

  .badge {
    position: absolute; border-radius: 50%; background: #fff;
    border: 6px solid var(--red);
    box-shadow: 0 0 0 7px var(--navy), 0 0 0 9px #fff;
    display: flex; flex-direction: column; align-items: center; justify-content: center;
    text-align: center; text-transform: uppercase; line-height: 1.05;
  }
  .badge--claims { width: 160px; height: 160px; left: 277px; top: 270px; font-size: 21px; color: var(--red); }
  .badge--claims .navy { color: var(--navy); }
  .badge--trial { width: 170px; height: 170px; left: 9px; top: 262px; font-size: 46px; color: var(--red); line-height: 1; }

  .offer {
    position: absolute; left: 12px; top: 488px; width: 430px;
    font-family: 'Oswald', sans-serif; font-weight: 400; color: var(--navy);
    text-transform: uppercase; font-size: 25px; line-height: 1.2;
    transform: rotate(-4deg); transform-origin: left top;
  }
  .offer b { font-weight: 600; }
  .offer .red { color: var(--red); font-weight: 600; }
  .offer .big { font-size: 33px; }

  .process {
    position: absolute; left: 10px; top: 480px; width: 436px;
    transform: rotate(1.5deg); transform-origin: left top;
    text-transform: uppercase;
  }
  .process .steps { font-family: 'Oswald', sans-serif; font-weight: 500; color: var(--navy); font-size: 19px; }
  .process .steps small { font-size: 15px; }
  .process .promise { color: var(--red); font-size: 19px; line-height: 1.3; }
  .process .promise small { font-size: 13px; }

  .brand {
    position: absolute; top: 595px; display: flex; align-items: center; gap: 8px;
  }
  .page--front .brand { left: 120px; }
  .page--back .brand { left: 118px; }
  .brand-dot { width: 34px; height: 34px; border-radius: 50%; background: var(--navy); }
  .brand-text { display: flex; flex-direction: column; }
  .brand-name { font-family: 'Oswald', sans-serif; font-weight: 700; font-size: 24px; color: var(--red); line-height: 1; letter-spacing: 1px; }
  .brand-tag { font-family: 'Questrial', sans-serif; font-size: 9px; color: var(--navy); letter-spacing: 1px; text-transform: uppercase; }
</style>
</head>
<body>

<section class="page page--front">
  <h1 class="headline">
    <span class="line1">It's your <span class="accent">money</span></span><br>
    <span class="line2">Get <span class="accent">it back!!</span></span>
  </h1>
  <div class="rule rule--top"></div>
  <div class="photo photo--train" role="img" aria-label="Commuters packed tightly inside a crowded UK train carriage"></div>
  <svg class="wave" viewBox="0 0 450 110" preserveAspectRatio="none" aria-hidden="true">
    <path d="M0 88 C150 70 300 40 450 10 L450 110 L0 110 Z" fill="#f5f3f8"/>
    <path d="M0 70 C150 52 300 22 450 -6 L450 10 C300 40 150 70 0 88 Z" fill="#d21f2b"/>
    <path d="M0 68 C150 50 300 20 450 -8" fill="none" stroke="#1c2a68" stroke-width="4"/>
  </svg>
  <div class="badge badge--claims">
    <span>No<br>claim<br>no fee!!</span>
    <span class="navy">Unlimited<br>claims!!</span>
  </div>
  <div class="rule rule--bottom"></div>
  <p class="offer">
    The <b>big deal</b> get up to <span class="red">40%</span> of cost of<br>
    ticket back' max of <span class="red big">£300 per month.</span>
  </p>
  <div class="brand">
    <span class="brand-dot"></span>
    <div class="brand-text">
      <span class="brand-name">FERROLIX</span>
      <span class="brand-tag">Train delay compensation</span>
    </div>
  </div>
</section>

<section class="page page--back">
  <h1 class="headline">
    <span class="line1">Download our app and</span><br>
    <span class="line2">We do <span class="accent">the rest!!</span></span>
  </h1>
  <div class="rule rule--top"></div>
  <div class="photo photo--station" role="img" aria-label="Commuters stranded on a busy UK station concourse under departure boards"></div>
  <svg class="wave" viewBox="0 0 450 110" preserveAspectRatio="none" aria-hidden="true">
    <path d="M0 10 C150 40 300 70 450 88 L450 110 L0 110 Z" fill="#f5f3f8"/>
    <path d="M0 -6 C150 22 300 52 450 70 L450 88 C300 70 150 40 0 10 Z" fill="#d21f2b"/>
    <path d="M0 -8 C150 20 300 50 450 68" fill="none" stroke="#1c2a68" stroke-width="4"/>
  </svg>
  <div class="badge badge--trial">Free<br>trial!</div>
  <div class="rule rule--bottom"></div>
  <div class="process">
    <p class="steps">No form filling <small>, No printing , No posting</small></p>
    <p class="promise"><small>We do all the </small>work just claim and wait <small>for your money through the</small> post.</p>
  </div>
  <div class="brand">
    <span class="brand-dot"></span>
    <div class="brand-text">
      <span class="brand-name">FERROLIX</span>
      <span class="brand-tag">Train delay compensation</span>
    </div>
  </div>
</section>

</body>
</html>
```